Loan broker seeks referral card design for real estate financing

We need a design for a referral card for people who recommend us for real estate financing. If the deal goes through, each referrer will receive €750.

Text similar to: Recommend me! For every successful real estate financing referral, you will receive €750. (Other suggestions are also welcome)

The size should be no larger than A5 format, or possibly even oblong.
The design should convey security and competence and include themes such as independent advice.

The design should also include the company logo and a photo of me. Naturally, the design should also include a link to my website: www.die-wandlinger.at, along with my phone number and email address: office@die-wandlinger.at

```html
<!DOCTYPE html>
<html lang="en">
<head>
<meta charset="utf-8">
<title>Referral card – Wandlinger Finanzberatung</title>
<link href="https://fonts.googleapis.com/css2?family=Space+Grotesk:wght@400;500;700&display=swap" rel="stylesheet">
<style>
  :root {
    --brand-blue: #1a56c4;
    --ink: #141a2a;
    --muted: #5b5f66;
    --paper: #ffffff;
    --tone-blue: #8fa9dc;
    --tone-light: #dfe6f4;
    --tone-grey: #c4c6cb;
    --photo-dark: #2a2734;
    --photo-shirt: #eceaf0;
    --photo-skin: #d9a48f;
    --photo-hair: #5a4a40;
  }
  * { margin: 0; padding: 0; box-sizing: border-box; }
  html, body { width: 1200px; height: 846px; overflow: hidden; background: var(--paper); }
  .card {
    position: relative;
    width: 1200px;
    height: 846px;
    background: var(--paper);
    font-family: "Space Grotesk", sans-serif;
    color: var(--ink);
    overflow: hidden;
  }
  .pattern-corner {
    position: absolute;
    left: 0; top: 0;
    width: 540px; height: 846px;
    background:
      linear-gradient(100deg, rgba(255,255,255,0) 30%, var(--paper) 92%),
      linear-gradient(180deg, var(--tone-grey) 0%, var(--tone-blue) 30%, var(--tone-light) 60%, var(--paper) 100%);
  }
  .pattern-band {
    position: absolute;
    left: 554px; top: 671px;
    width: 646px; height: 175px;
    background: linear-gradient(90deg, var(--tone-grey) 0%, var(--tone-light) 35%, var(--tone-grey) 65%, var(--tone-light) 100%);
  }
  .portrait {
    position: absolute;
    left: 0; top: 0;
    width: 1200px; height: 846px;
  }
  .brand {
    position: absolute;
    left: 549px; top: 72px;
    display: flex; align-items: center; gap: 18px;
  }
  .brand-mark {
    width: 92px; height: 92px;
    border: 3px solid var(--brand-blue);
    border-radius: 50%;
  }
  .brand-text { display: flex; flex-direction: column; gap: 4px; }
  .brand-name {
    font-size: 17px;
    font-weight: 700;
    color: var(--brand-blue);
  }
  .brand-tagline {
    font-size: 13px;
    font-weight: 500;
    color: var(--muted);
  }
  .headline {
    position: absolute;
    left: 548px; top: 222px;
    font-size: 68px;
    font-weight: 700;
    letter-spacing: -0.5px;
    color: var(--brand-blue);
    line-height: 1;
  }
  .offer {
    position: absolute;
    left: 550px; top: 328px;
    font-size: 30px;
    line-height: 43px;
    font-weight: 400;
    letter-spacing: 0.3px;
  }
  .offer strong { font-weight: 700; }
  .contact {
    position: absolute;
    left: 550px; top: 511px;
    list-style: none;
    font-size: 22px;
    font-weight: 700;
    line-height: 36px;
    color: var(--brand-blue);
  }
</style>
</head>
<body>
  <main class="card">
    <div class="pattern-corner" role="img" aria-label="Decorative pattern of blue and grey triangles"></div>
    <div class="pattern-band" role="img" aria-label="Decorative band of blue and grey triangles"></div>

    <svg class="portrait" viewBox="0 0 1200 846" role="img" aria-label="Portrait photo of the financial adviser in a dark suit and white shirt">
      <defs>
        <linearGradient id="portrait-tones" x1="0" y1="168" x2="0" y2="846" gradientUnits="userSpaceOnUse">
          <stop offset="0" stop-color="var(--photo-hair)"/>
          <stop offset="0.1" stop-color="var(--photo-skin)"/>
          <stop offset="0.6" stop-color="var(--photo-skin)"/>
          <stop offset="0.7" stop-color="var(--photo-shirt)"/>
          <stop offset="0.82" stop-color="var(--photo-dark)"/>
          <stop offset="1" stop-color="var(--photo-dark)"/>
        </linearGradient>
      </defs>
      <path fill="url(#portrait-tones)" d="M45 330 C60 220 140 168 240 168 C340 168 400 230 410 390 L415 500 C400 560 400 580 420 595 L530 655 C620 690 670 760 690 846 L0 846 L0 780 C40 700 60 620 50 560 Z"/>
    </svg>

    <header class="brand">
      <span class="brand-mark"></span>
      <span class="brand-text">
        <span class="brand-name">Wandlinger Finanzberatung GmbH</span>
        <span class="brand-tagline">Finanzieren, Versichern, Vorsorgen</span>
      </span>
    </header>

    <h1 class="headline">Recommend me!</h1>
    <p class="offer">For every successful real<br>estate financing referral,<br><strong>you will receive €750.</strong></p>

    <ul class="contact">
      <li>+43 660 214 5098</li>
      <li>office@die-wandlinger.at</li>
      <li>www.die-wandlinger.at</li>
    </ul>
  </main>
</body>
</html>
```